Signage Design Project

I am looking for a real estate sign that we would use in front of our high end properties. We are based in Southern California. The size of the sign will be 18x24.
Our company colors are blue and grey . You may view our websites at www.borlanexinc.com & www.borlanexrealty.com. The name and information on the sign should be:
Exclusively offered by
Borlanex keystone properties
Www.borlanexrealty.com
800-462-5183
Updates
Project Deadline Extended
Reason: In order to give you more time to come up with a high end retail residential look.
Target Market(s)
Southern California coastal area with property values above $1 million
Industry/Entity Type
Real Estate
Look and feel
Each slider illustrates characteristics of the customer's brand and the style your logo design should communicate.

```html
<!DOCTYPE html>
<html lang="en">
<head>
<meta charset="utf-8">
<title>Borlanex Keystone Properties – Yard Sign</title>
<link rel="stylesheet" href="https://fonts.googleapis.com/css2?family=Cinzel:wght@400;600;700&family=EB+Garamond:wght@500&family=Marcellus&display=swap">
<style>
  :root {
    --ink: #0d0d0d;
    --paper: #ffffff;
    --brand-blue: #2a84ff;
    --hairline-blue: #9cc3e8;
    --hairline-grey: #8a8a8a;
    --bar-grey: #3a3a3a;
  }
  * { margin: 0; padding: 0; box-sizing: border-box; }
  html, body {
    width: 1200px; height: 969px; overflow: hidden;
    background: var(--paper);
  }
  .sign {
    position: relative; width: 1200px; height: 969px;
    background: var(--paper); color: var(--ink);
  }
  .sign__edge {
    position: absolute; left: 3px; top: 3px; width: 1194px; height: 897px;
    border: 1.5px solid var(--hairline-grey);
  }
  .sign__frame-outer {
    position: absolute; left: 19px; top: 19px; width: 1162px; height: 866px;
    border: 9px solid var(--ink);
  }
  .sign__frame-inner {
    position: absolute; left: 33px; top: 33px; width: 1134px; height: 838px;
    border: 5px solid var(--ink);
  }
  .sign__frame-accent {
    position: absolute; left: 42px; top: 42px; width: 1116px; height: 820px;
    border: 1.5px solid var(--hairline-blue);
  }
  .brand-mark {
    position: absolute; left: 515px; top: 84px; width: 170px; height: 170px;
    background: var(--brand-blue);
  }
  .line {
    position: absolute; left: 0; width: 100%;
    text-align: center; line-height: 1; white-space: nowrap;
  }
  .offer {
    top: 312px; font-family: "EB Garamond", serif; font-weight: 500;
    font-size: 44px; letter-spacing: 0.02em;
  }
  .brand-name {
    top: 372px; font-family: "Cinzel", serif; font-weight: 400;
    font-size: 172px; letter-spacing: 0.01em;
  }
  .brand-tagline {
    top: 553px; font-family: "Cinzel", serif; font-weight: 400;
    font-size: 36px; letter-spacing: 0.2em;
  }
  .agent {
    top: 630px; display: flex; justify-content: center; align-items: center; gap: 16px;
  }
  .agent__bar { width: 86px; height: 12px; }
  .agent__bar polygon { fill: var(--bar-grey); }
  .agent__name {
    font-family: "Cinzel", serif; font-weight: 600;
    font-size: 28px; letter-spacing: 0.08em;
  }
  .phone {
    top: 719px; font-family: "Marcellus", serif;
    font-size: 52px; letter-spacing: 0.03em;
  }
  .website {
    top: 773px; font-family: "Cinzel", serif; font-weight: 700;
    font-size: 40px; letter-spacing: 0.08em;
  }
</style>
</head>
<body>
  <main class="sign">
    <div class="sign__edge"></div>
    <div class="sign__frame-outer"></div>
    <div class="sign__frame-inner"></div>
    <div class="sign__frame-accent"></div>

    <div class="brand-mark" aria-hidden="true"></div>

    <p class="line offer">Exclusively offered by</p>
    <h1 class="line brand-name">BORLANEX</h1>
    <p class="line brand-tagline">KEYSTONE PROPERTIES</p>

    <div class="line agent">
      <svg class="agent__bar" viewBox="0 0 86 12" aria-hidden="true"><polygon points="0,6 86,0 86,12"/></svg>
      <span class="agent__name">Dean Whitmore</span>
      <svg class="agent__bar" viewBox="0 0 86 12" aria-hidden="true"><polygon points="0,0 86,6 0,12"/></svg>
    </div>

    <p class="line phone">800-462-5183</p>
    <p class="line website">WWW.BORLANEXREALTY.COM</p>
  </main>
</body>
</html>
```